Site for a workout and Consulting enterprise

I need a professional responsive site for www.olvaru.hamburg. The website shoulderstand consist of a Landing and 4 other pages. - On page for the contact informations - on page for the about - on page for consulting services (technical) - on page for Training and workshop services (business and soft skills) I add some files so you can see my idea of the design.
Target Market(s)
IT and Management
Industry/Entity Type
Management Consulting
Coding
Coded - Design and coding required
Number of Pages Required
4 page
Requirements
Must have
- Use Pictures for Background, Sliders and Topics. Just have to placeholders for the design.

```html
<!DOCTYPE html>
<html lang="de">
<head>
<meta charset="utf-8">
<title>olvaru – Individuen, Ideen, Innovationen</title>
<link href="https://fonts.googleapis.com/css2?family=Roboto:wght@300;400;500;700&display=swap" rel="stylesheet">
<style>
:root{
  --navy:#0b2f5c;
  --navy-deep:#0a2547;
  --footer:#0d2b4f;
  --charcoal:#4a4a4a;
  --bar:#575757;
  --ink:#333;
  --muted:#555;
  --white:#fff;
  --line:#c9ced6;
}
*{box-sizing:border-box;margin:0;padding:0}
html,body{width:1200px;height:3214px;overflow:hidden}
body{font-family:'Roboto',Arial,sans-serif;color:var(--ink);background:var(--white);position:relative}
a{color:inherit;text-decoration:none}

.site-header{position:absolute;left:0;top:0;width:1200px;height:116px;background:var(--white);box-shadow:0 2px 6px rgba(0,0,0,.12);z-index:2}
.brand{position:absolute;left:80px;top:16px;display:flex;flex-direction:column}
.brand-row{display:flex;align-items:center;gap:10px}
.brand-square{width:34px;height:34px;background:var(--navy)}
.brand-name{font-size:42px;font-weight:500;color:var(--navy);line-height:1}
.brand-tagline{font-size:15px;color:var(--navy);margin-top:6px}
.header-phone{position:absolute;right:80px;top:24px;display:flex;align-items:center;gap:10px;font-size:19px;color:var(--ink)}
.main-nav{position:absolute;right:80px;top:62px;display:flex;gap:18px;font-size:16px;color:var(--ink)}
.main-nav .active{color:var(--navy);font-weight:500}

.hero{position:absolute;left:0;top:116px;width:1200px;height:535px;
  background:linear-gradient(90deg,#eef1f4 0%,#e4e8ec 45%,#c9d1d8 70%,#b98a8a 85%,#d9d6d6 100%)}
.hero-title{position:absolute;left:78px;top:112px;font-size:64px;font-weight:400;color:var(--navy);line-height:1}
.hero-subtitle{position:absolute;left:78px;top:194px;font-size:52px;font-weight:300;color:var(--navy);line-height:1}
.hero-text{position:absolute;left:80px;top:264px;width:590px;font-size:13.5px;line-height:24px;color:var(--muted)}
.btn-solid{position:absolute;left:80px;top:366px;width:177px;height:44px;border-radius:22px;background:var(--navy);color:var(--white);font-size:15px;display:flex;align-items:center;justify-content:center}

.about{position:absolute;left:0;top:651px;width:1200px;height:583px;background:var(--white)}
.section-title-center{position:absolute;left:0;width:1200px;top:48px;text-align:center;font-size:36px;font-weight:400;color:var(--navy)}
.title-rule-center{position:absolute;left:570px;top:104px;width:60px;height:3px;background:var(--navy)}
.about-text{position:absolute;left:100px;width:1000px;text-align:center;font-size:13.5px;line-height:27px;color:var(--muted)}
.about-band{position:absolute;left:0;top:367px;width:1200px;height:200px;
  background:linear-gradient(180deg,#ffffff 0%,#e8eef4 40%,#cfd8e2 80%,#ffffff 100%)}

.service{position:absolute;left:0;width:1200px;height:510px}
.service-photo{position:absolute;top:0;width:600px;height:100%}
.service-panel{position:absolute;top:0;width:600px;height:100%;color:var(--white)}
.consulting{top:1234px}
.consulting .service-photo{left:0;background:linear-gradient(135deg,#5b4a3a 0%,#8a7256 45%,#6d5a46 100%)}
.consulting .service-panel{left:600px;background:var(--navy)}
.training{top:1744px}
.training .service-panel{left:0;background:var(--charcoal)}
.training .service-photo{left:600px;background:linear-gradient(180deg,#6f7d93 0%,#c6905a 50%,#8a5a3c 75%,#6b4b34 100%)}
.panel-inner{position:absolute;left:60px;top:50px;width:460px}
.training .panel-inner{left:80px}
.panel-title{font-size:32px;font-weight:400;line-height:1.1}
.panel-rule{width:60px;height:3px;background:var(--white);margin:12px 0 22px}
.panel-text{font-size:13.5px;line-height:27px}
.btn-light{display:flex;align-items:center;justify-content:center;width:178px;height:44px;border-radius:22px;background:var(--white);color:var(--navy);font-size:15px;margin-top:36px}
.panel-footer-photo{position:absolute;left:0;bottom:0;width:600px;height:80px;background:linear-gradient(180deg,rgba(74,74,74,0) 0%,#5a3b3b 100%)}

.contact{position:absolute;left:0;top:2254px;width:1200px;height:547px;
  background:linear-gradient(90deg,#ffffff 0%,#ffffff 40%,#eef1f4 55%,#d9dfe5 75%,#c7ced6 100%)}
.section-title-left{position:absolute;left:80px;top:62px;font-size:32px;font-weight:400;color:var(--navy)}
.title-rule-left{position:absolute;left:80px;top:110px;width:40px;height:3px;background:var(--navy)}
.contact-form{position:absolute;left:81px;top:140px;width:358px}
.field{width:100%;height:46px;border:1px solid var(--line);background:var(--white);border-radius:3px;font-size:12px;color:#888;padding:14px 12px;margin-bottom:8px}
.field-message{height:100px}
.btn-submit{width:100%;height:46px;background:var(--navy);color:var(--white);font-size:19px;display:flex;align-items:center;justify-content:center;border-radius:2px;margin-top:4px}

.site-footer{position:absolute;left:0;top:2801px;width:1200px;height:339px;background:var(--footer);color:var(--white)}
.footer-col{position:absolute;top:74px}
.footer-heading{font-size:17px;font-weight:400;padding-bottom:10px;border-bottom:1px solid rgba(255,255,255,.25);margin-bottom:16px}
.footer-links li{list-style:none;font-size:13px;line-height:27px}
.footer-links li::before{content:"›";margin-right:7px}
.footer-small{font-size:12px;line-height:17px}
.info-line{display:flex;align-items:center;gap:10px;font-size:13px;margin-top:16px}
.newsletter-input{margin-top:16px;width:200px;height:26px;background:var(--white);color:#888;font-size:11px;padding:6px 8px}
.btn-subscribe{margin-top:12px;width:76px;height:24px;background:#6f7b88;font-size:11px;display:flex;align-items:center;justify-content:center}
.social-item{display:flex;align-items:center;gap:12px;font-size:13px;line-height:24px;margin-bottom:10px}
.social-square{width:22px;height:22px;background:#4c6a8f}
.copyright-bar{position:absolute;left:0;top:3140px;width:1200px;height:74px;background:var(--bar);color:#eee;font-size:13px;display:flex;align-items:center;justify-content:center}
</style>
</head>
<body>

<header class="site-header">
  <div class="brand">
    <div class="brand-row"><span class="brand-square"></span><span class="brand-name">olvaru</span></div>
    <span class="brand-tagline">Individuen, Ideen, Innovationen</span>
  </div>
  <div class="header-phone">
    <svg width="24" height="24" viewBox="0 0 24 24"><circle cx="12" cy="12" r="11" fill="none" stroke="#333" stroke-width="1.6"/><path d="M8.5 7c.6-.6 1.3-.4 1.6.2l.9 1.6c.3.5.1 1-.3 1.3l-.5.4c.5 1.3 1.4 2.3 2.7 2.9l.4-.5c.3-.4.9-.5 1.3-.2l1.6.9c.6.3.8 1 .2 1.6-1 1-2.6 1.1-4.2.1-1.7-1-3.1-2.5-4-4.2-.8-1.5-.7-3.1.3-4.1z" fill="#333"/></svg>
    <span>555 014 2290</span>
  </div>
  <nav class="main-nav">
    <a class="active" href="#">Home</a><a href="#">About Us</a><a href="#">Consulting Services</a><a href="#">Training &amp; Workshop Services</a><a href="#">Impressum</a><a href="#">Contact Us</a>
  </nav>
</header>

<section class="hero" role="img" aria-label="Bright room with large window, a pillow on the sill and a child in a red cape leaping like a superhero">
  <h1 class="hero-title">Individuen</h1>
  <p class="hero-subtitle">Ideen &amp; Innovationen</p>
  <p class="hero-text">Maecenas sit amet felis odio. Curabitur condimentum lacinia nulla ac ultrices. Ut convallis magna sit amet congue malesuada. Nam ullamcorper, lectus nec laoreet viverra, metus tortor aliquam purus, sed aliquam arcu massa eu mauris.</p>
  <a class="btn-solid" href="#">Contact Us</a>
</section>

<section class="about">
  <h2 class="section-title-center">About Us</h2>
  <span class="title-rule-center"></span>
  <p class="about-text" style="top:136px">Lorem ipsum dolor sit amet, consectetur adipiscing elit. Morbi accumsan velit purus, sed tempus odio tempus ac. Suspendisse vitae diam volutpat, tempor enim at, facilisis augue. Praesent dictum eros sed placerat accumsan. Cras lobortis hendrerit ornare. Cras vulputate nec mi in vulputate. Proin finibus, lorem ut lobortis iaculis, lectus ligula accumsan erat, at feugiat nulla erat vitae tellus.</p>
  <p class="about-text" style="top:243px">In vehicula commodo metus, et pellentesque ipsum rhoncus non. Vestibulum rhoncus justo aliquam erat rutrum accumsan. Integer enim mauris, sodales sed ultricies at, facilisis et leo. Proin consectetur, augue id hendrerit condimentum, augue sem tristique nibh, vel volutpat dui leo eu magna. In mattis odio quis velit convallis, vel dapibus enim sodales. Integer imperdiet elit eget velit egestas ullamcorper.</p>
  <div class="about-band" role="img" aria-label="Row of business people silhouettes standing between blue gear wheels"></div>
</section>

<section class="service consulting">
  <div class="service-photo" role="img" aria-label="Hands arranging wooden blocks, puzzle pieces and a light bulb sketch on a wooden table"></div>
  <div class="service-panel">
    <div class="panel-inner">
      <h2 class="panel-title">Consulting Services</h2>
      <div class="panel-rule"></div>
      <p class="panel-text">Etiam id enim enim. Nulla interdum velit nec egestas consequat. Proin id varius massa, nec pharetra nibh. Mauris condimentum imperdiet lectus vitae vehicula. Donec quis congue elit, nec hendrerit orci. Nam quis ex nibh. Sed pharetra vitae magna in rutrum. Integer vestibulum purus vel purus iaculis, id hendrerit turpis gravida. Cras et pharetra enim. Nunc vel leo erat. Nunc ex leo, accumsan nec fringilla id, ornare et urna.</p>
      <a class="btn-light" href="#">Learn More...</a>
    </div>
  </div>
</section>

<section class="service training">
  <div class="service-panel">
    <div class="panel-inner">
      <h2 class="panel-title">Training &amp; Workshop Services</h2>
      <div class="panel-rule"></div>
      <p class="panel-text">Etiam id enim enim. Nulla interdum velit nec egestas consequat. Proin id varius massa, nec pharetra nibh. Mauris condimentum imperdiet lectus vitae vehicula. Donec quis congue elit, nec hendrerit orci. Nam quis ex nibh. Sed pharetra vitae magna in rutrum. Integer vestibulum purus vel purus iaculis, id hendrerit turpis gravida. Cras et pharetra enim. Nunc vel leo erat. Nunc ex leo, accumsan nec fringilla id, ornare et urna.</p>
      <a class="btn-light" href="#">Learn More...</a>
    </div>
    <div class="panel-footer-photo" role="img" aria-label="Hands holding up red letters that spell a motivational phrase"></div>
  </div>
  <div class="service-photo" role="img" aria-label="Stack of old books on a wooden pier at sunset by the sea"></div>
</section>

<section class="contact" role="img" aria-label="Smiling man working on a laptop at a white desk with a lamp and a plant">
  <h2 class="section-title-left">Contact Us</h2>
  <span class="title-rule-left"></span>
  <form class="contact-form">
    <div class="field">Name:</div>
    <div class="field">Email Address:</div>
    <div class="field">Phone Number:</div>
    <div class="field field-message">Message:</div>
    <div class="btn-submit">Submit</div>
  </form>
</section>

<footer class="site-footer">
  <div class="footer-col" style="left:79px;width:170px">
    <h3 class="footer-heading">Quick Links</h3>
    <ul class="footer-links">
      <li>Home</li><li>About Us</li><li>Consulting Services</li><li>Training &amp; Workshop Services</li><li>Impressum</li><li>Contact Us</li>
    </ul>
  </div>
  <div class="footer-col" style="left:321px;width:270px">
    <h3 class="footer-heading">Contact Information</h3>
    <p class="footer-small">Supendisse convallis ex eu velit dapibus erat consequat.</p>
    <div class="info-line"><svg width="14" height="16" viewBox="0 0 14 16"><path d="M7 0a6 6 0 0 0-6 6c0 4.5 6 10 6 10s6-5.5 6-10a6 6 0 0 0-6-6zm0 8.5A2.5 2.5 0 1 1 7 3.5a2.5 2.5 0 0 1 0 5z" fill="#fff"/></svg>18 Elbufer Street, Hamburg</div>
    <div class="info-line"><svg width="14" height="16" viewBox="0 0 24 24"><path d="M6 2c1-1 2.2-.7 2.7.3l1.5 2.7c.5.9.2 1.7-.5 2.2l-.9.7c.9 2.2 2.4 3.9 4.6 4.9l.7-.9c.5-.7 1.5-.9 2.2-.4l2.7 1.5c1 .5 1.3 1.7.3 2.7-1.7 1.7-4.4 1.9-7.1.2C9.4 14 7 11.5 5.5 8.6 4.1 6 4.3 3.7 6 2z" fill="#fff"/></svg>555 017 3361</div>
    <div class="info-line"><svg width="14" height="11" viewBox="0 0 14 11"><rect x="0.5" y="0.5" width="13" height="10" fill="none" stroke="#fff"/><path d="M.5.5 7 6 13.5.5" fill="none" stroke="#fff"/></svg>info@olvaru.hamburg</div>
  </div>
  <div class="footer-col" style="left:658px;width:240px">
    <h3 class="footer-heading">Newsletter Signup</h3>
    <p class="footer-small">Please enter your email address below to receive our FREE newsletter</p>
    <div class="newsletter-input">Your Email ID</div>
    <div class="btn-subscribe">Subscribe</div>
  </div>
  <div class="footer-col" style="left:951px;width:170px">
    <h3 class="footer-heading">Follow Us</h3>
    <div class="social-item"><span class="social-square"></span>Community</div>
    <div class="social-item"><span class="social-square"></span>Network</div>
    <div class="social-item"><span class="social-square"></span>Updates</div>
    <div class="social-item"><span class="social-square"></span>Email</div>
  </div>
</footer>

<div class="copyright-bar">© 2017 olvaru.hamburg. All Rights Are Reserved.</div>

</body>
</html>
```